Web Design Project for Communications Agency

The design I need (PSD file) is for an agency offering specialised PR and communications services for customers in the healthcare sector.

OBJECTIVES OF THE WEBSITE:
1. To promote the agency's communication services
2. To position Solène Verbruggen as an industry leader, an expert in healthcare PR and communications by highlighting blogposts and social media.

WHAT I NEED:
1st, I need the design for the Home Page ONLY.
Once approved, I will need the other pages designed as well. (Here is prototype that we've already developed for the Website that will guide you in the design:
http://qoravenlab.com/solenverbruggen/)

VISUAL INSPIRATION
We want to give this Website a "Flat Design" look. Here are some websites for inspiration :
- http://lumbrafolk.com/#!/process
- http://www.quillmarsh.co/
- http://dorvellink.com/

Also, reuse images found on the company's current Website :
http://www.solenverbruggen.com/fr/index.html

HOMEPAGE MAIN ELEMENTS:
1. Main menu : 6 sections
Accueil | Agence | Services | Approche | Publications | Contact

2. Main Call To Action (big dark rectangle in prototype):
Can be slider or just an information bloc.

3. Publications récentes :
The 4 latest blog posts must be features on the homepage (will be linked with the "Publications" section)

4. Dynamic Footer :
Contains a Chirpline feed and a Subscribe to our Newsletter feature (revecez nos publications)

OTHER PAGES (to design once Homepage is approved)
- Agence (about us)
- Services (our team)
- Approche (our approach)
- Publications (blog articles)
- Contact (Contact us)

• Please refer to prototype :
http://qoravenlab.com/solenverbruggen/
Must have ALL features present in prototype.

Also, must reuse this picture in the design : http://solenverbruggen.com/static/images/home-big-box.jpg

Finally, you will find attached the company logo.

```html
<!DOCTYPE html>
<html lang="fr">
<head>
<meta charset="utf-8">
<title>Solène Verbruggen – Gestion d'enjeux et affaires publiques</title>
<link rel="stylesheet" href="https://fonts.googleapis.com/css2?family=Titillium+Web:wght@200;300;400;600;700&family=Open+Sans:wght@400;600;700&display=swap">
<style>
:root{
  --red:#e8503a;
  --red-dark:#d8442f;
  --white:#ffffff;
  --hero:#ededed;
  --ink:#3a3a3a;
  --muted:#8a8a8a;
  --rule:#e4e4e4;
  --footer:#4b4b4b;
  --footer-field:#3c3c3c;
  --footer-text:#cfcfcf;
}
*{margin:0;padding:0;box-sizing:border-box}
html,body{width:1200px;height:2218px;overflow:hidden}
body{position:relative;background:var(--white);font-family:"Open Sans",Arial,sans-serif;color:var(--ink)}
.abs{position:absolute}

/* header */
.brand-band{left:0;top:0;width:1200px;height:160px;background:var(--red)}
.brand-name{left:148px;top:22px;width:240px;color:var(--white);font-family:"Titillium Web",Arial,sans-serif;font-weight:300;font-size:50px;line-height:50px;text-transform:lowercase}
.nav-bar{left:0;top:160px;width:1200px;height:54px;background:var(--white);border-bottom:1px solid var(--rule)}
.tagline{left:148px;top:170px;font-family:"Titillium Web",Arial,sans-serif;font-weight:700;font-size:12px;line-height:14px;letter-spacing:.5px;color:#333;border-top:2px solid var(--red);border-bottom:2px solid var(--red);padding:2px 0}
.tagline span{display:block}
.tagline span+span{font-weight:400}
.main-nav{left:320px;top:160px;width:780px;height:54px;display:flex;list-style:none}
.main-nav li{flex:1;text-align:center;line-height:54px;font-family:"Titillium Web",Arial,sans-serif;font-size:14px;color:#9a9a9a;text-transform:uppercase;letter-spacing:.5px}
.main-nav li.active{color:var(--red)}

/* hero */
.hero{left:0;top:214px;width:1200px;height:382px;background:var(--hero)}
.hero-title{left:148px;top:278px;font-family:"Titillium Web",Arial,sans-serif;font-weight:300;font-size:62px;line-height:80px;color:var(--red)}
.hero-lead{left:148px;top:362px;width:520px;font-family:"Titillium Web",Arial,sans-serif;font-weight:300;font-size:24px;line-height:32px;color:#555}
.hero-lead em{font-style:normal;color:var(--red)}
.btn{background:var(--red);color:var(--white);font-family:"Open Sans",Arial,sans-serif;font-weight:700;text-align:center;border-radius:2px}
.hero-btn{left:148px;top:463px;width:175px;height:50px;line-height:50px;font-size:14px;box-shadow:0 3px 0 var(--red-dark)}
.hero-visual{left:678px;top:234px;width:406px;height:334px;background:radial-gradient(ellipse at 50% 40%,#fafafa 0%,#e2e2e2 55%,rgba(237,237,237,0) 75%)}
.notch{width:0;height:0;border-left:14px solid transparent;border-right:14px solid transparent}
.hero-notch{left:392px;top:596px;border-top:14px solid var(--hero)}

/* publications */
.section-title{left:148px;top:620px;font-family:"Titillium Web",Arial,sans-serif;font-weight:400;font-size:20px;color:var(--red);text-transform:uppercase}
.post{left:148px;width:904px;height:278px}
.post-thumb{left:22px;top:0;width:170px;height:138px}
.post-date{left:22px;top:164px;width:170px;text-align:center;font-size:11px;color:var(--muted)}
.post-title{left:288px;top:0;font-size:13px;font-weight:700;color:#222;text-decoration:underline}
.post-body{left:288px;top:24px;width:616px;font-size:12.5px;line-height:21px;color:#555;text-align:justify}
.post-body p+p{margin-top:21px}
.post-more{right:0;top:200px;font-size:14px;font-weight:700;color:var(--red)}
.post-rule{left:22px;top:231px;width:882px;height:1px;background:var(--rule)}

/* footer */
.footer{left:0;top:1799px;width:1200px;height:419px;background:var(--footer)}
.footer-notch{left:380px;top:1799px;border-top:14px solid var(--white)}
.feed-name{left:153px;top:1830px;font-family:"Titillium Web",Arial,sans-serif;font-weight:700;font-size:24px;color:var(--white)}
.tweet{left:153px;width:245px;height:60px}
.tweet-avatar{left:0;top:0;width:54px;height:48px;background:linear-gradient(#c99b7d,#9c6f55)}
.tweet-text{left:79px;top:0;width:166px;font-size:9.5px;line-height:12px;color:var(--footer-text)}
.tweet-text span{color:var(--red)}
.follow-btn{left:153px;top:2136px;width:185px;height:37px;line-height:37px;font-size:11px}
.signup-title{left:468px;top:1830px;font-family:"Titillium Web",Arial,sans-serif;font-weight:300;font-size:22px;color:var(--white);text-transform:uppercase}
.signup-rule{left:468px;top:1873px;width:584px;height:1px;background:#5e5e5e}
.field{left:468px;width:584px;height:42px;background:var(--footer-field);color:#8d8d8d;font-size:11px;line-height:42px;padding-left:14px}
.signup-btn{left:468px;top:2028px;width:128px;height:39px;line-height:39px;font-size:11px;font-weight:400}
.copyright{left:931px;top:2150px;font-size:9px;line-height:12px;color:#7e7e7e}
</style>
</head>
<body>

<header>
  <div class="abs brand-band"></div>
  <div class="abs brand-name">solène<br>verbruggen</div>
  <div class="abs nav-bar"></div>
  <div class="abs tagline"><span>GESTION D'ENJEUX</span><span>AFFAIRES PUBLIQUES</span></div>
  <ul class="abs main-nav">
    <li class="active">Agence</li>
    <li>Services</li>
    <li>Approche</li>
    <li>Publications</li>
    <li>Contact</li>
  </ul>
</header>

<section>
  <div class="abs hero"></div>
  <h1 class="abs hero-title">Solène Verbruggen//</h1>
  <p class="abs hero-lead"><em>Cabinet-conseil</em> en communications et affaires publiques spécialisé dans le <em>secteur de la santé.</em></p>
  <div class="abs btn hero-btn">En Savoir Plus &nbsp;›</div>
  <div class="abs hero-visual" role="img" aria-label="Grand cube blanc portant une croix rouge sur sa face supérieure"></div>
  <div class="abs notch hero-notch"></div>
</section>

<main>
  <h2 class="abs section-title">Publication récentes</h2>

  <article class="abs post" style="top:685px">
    <div class="abs post-thumb" role="img" aria-label="Main tenant un téléphone affichant un graphique" style="background:linear-gradient(135deg,#6d7c8c,#c9cfd6)"></div>
    <div class="abs post-date">23 Juillet 2013</div>
    <h3 class="abs post-title">Titre de la publication</h3>
    <div class="abs post-body"><p>Lorem ipsum dolor sit amet, consectetur adipisicing elit, sed do eiusmod tempor incididunt ut labore et dolore magna aliqua. Ut enim ad minim veniam, quis nostrud exercitation ullamco laboris nisi ut aliquip ex ea commodo consequat. Duis aute irure dolor in reprehenderit in voluptate velit esse cillum dolore eu fugiat nulla pariatur. Excepteur sint occaecat cupidatat non proident, sunt in culpa qui officia deserunt mollit anim id est laborum.</p><p>Velit esse cillum dolore eu fugiat nulla pariatur. Excepteur sint occaecat cupidatat non proident, sunt in culpa qui officia deserunt mollit anim id est laborum.</p></div>
    <div class="abs post-more">Article complet &nbsp;+</div>
    <div class="abs post-rule"></div>
  </article>

  <article class="abs post" style="top:963px">
    <div class="abs post-thumb" role="img" aria-label="Personne assise dans un intérieur sombre" style="background:linear-gradient(135deg,#3a2a22,#8a6a52)"></div>
    <div class="abs post-date">23 Juillet 2013</div>
    <h3 class="abs post-title">Titre de la publication</h3>
    <div class="abs post-body"><p>Lorem ipsum dolor sit amet, consectetur adipisicing elit, sed do eiusmod tempor incididunt ut labore et dolore magna aliqua. Ut enim ad minim veniam, quis nostrud exercitation ullamco laboris nisi ut aliquip ex ea commodo consequat. Duis aute irure dolor in reprehenderit in voluptate velit esse cillum dolore eu fugiat nulla pariatur. Excepteur sint occaecat cupidatat non proident, sunt in culpa qui officia deserunt mollit anim id est laborum.</p><p>Velit esse cillum dolore eu fugiat nulla pariatur. Excepteur sint occaecat cupidatat non proident, sunt in culpa qui officia deserunt mollit anim id est laborum.</p></div>
    <div class="abs post-more">Article complet &nbsp;+</div>
    <div class="abs post-rule"></div>
  </article>

  <article class="abs post" style="top:1242px">
    <div class="abs post-thumb" role="img" aria-label="Coussin décoré posé sur un fauteuil" style="background:linear-gradient(135deg,#4a2c24,#b89a86)"></div>
    <div class="abs post-date">23 Juillet 2013</div>
    <h3 class="abs post-title">Titre de la publication</h3>
    <div class="abs post-body"><p>Lorem ipsum dolor sit amet, consectetur adipisicing elit, sed do eiusmod tempor incididunt ut labore et dolore magna aliqua. Ut enim ad minim veniam, quis nostrud exercitation ullamco laboris nisi ut aliquip ex ea commodo consequat. Duis aute irure dolor in reprehenderit in voluptate velit esse cillum dolore eu fugiat nulla pariatur. Excepteur sint occaecat cupidatat non proident, sunt in culpa qui officia deserunt mollit anim id est laborum.</p><p>Velit esse cillum dolore eu fugiat nulla pariatur. Excepteur sint occaecat cupidatat non proident, sunt in culpa qui officia deserunt mollit anim id est laborum.</p></div>
    <div class="abs post-more">Article complet &nbsp;+</div>
    <div class="abs post-rule"></div>
  </article>

  <article class="abs post" style="top:1523px">
    <div class="abs post-thumb" role="img" aria-label="Portrait d'un homme souriant" style="background:linear-gradient(135deg,#2f4256,#c9a58a)"></div>
    <div class="abs post-date">23 Juillet 2013</div>
    <h3 class="abs post-title">Titre de la publication</h3>
    <div class="abs post-body"><p>Lorem ipsum dolor sit amet, consectetur adipisicing elit, sed do eiusmod tempor incididunt ut labore et dolore magna aliqua. Ut enim ad minim veniam, quis nostrud exercitation ullamco laboris nisi ut aliquip ex ea commodo consequat. Duis aute irure dolor in reprehenderit in voluptate velit esse cillum dolore eu fugiat nulla pariatur. Excepteur sint occaecat cupidatat non proident, sunt in culpa qui officia deserunt mollit anim id est laborum.</p><p>Velit esse cillum dolore eu fugiat nulla pariatur. Excepteur sint occaecat cupidatat non proident, sunt in culpa qui officia deserunt mollit anim id est laborum.</p></div>
    <div class="abs post-more">Article complet &nbsp;+</div>
  </article>
</main>

<footer>
  <div class="abs footer"></div>
  <div class="abs notch footer-notch"></div>
  <div class="abs feed-name">chirpline</div>

  <div class="abs tweet" style="top:1897px">
    <div class="abs tweet-avatar" role="img" aria-label="Photo de profil"></div>
    <p class="abs tweet-text">Velit esse cillum dolore eu fugiat nulla pariatur. Excepteur sint occaecat cupidatat non proident.<br><span>#santé #veille #enjeux</span></p>
  </div>
  <div class="abs tweet" style="top:1966px">
    <div class="abs tweet-avatar" role="img" aria-label="Photo de profil"></div>
    <p class="abs tweet-text">Velit esse cillum dolore eu fugiat nulla pariatur. Excepteur sint occaecat cupidatat non proident.<br><span>#santé #veille #enjeux</span></p>
  </div>
  <div class="abs tweet" style="top:2035px">
    <div class="abs tweet-avatar" role="img" aria-label="Photo de profil"></div>
    <p class="abs tweet-text">Velit esse cillum dolore eu fugiat nulla pariatur. Excepteur sint occaecat cupidatat non proident.<br><span>#santé #veille #enjeux</span></p>
  </div>
  <div class="abs btn follow-btn">Suivre @SVerbruggen</div>

  <h2 class="abs signup-title">Recevez nos publications</h2>
  <div class="abs signup-rule"></div>
  <div class="abs field" style="top:1902px">Votre nom</div>
  <div class="abs field" style="top:1961px">Votre courriel</div>
  <div class="abs btn signup-btn">Abonnez-vous</div>

  <p class="abs copyright">© 2013 Solène Verbruggen<br>Tous droits réservés</p>
</footer>

</body>
</html>
```